CRPG is needing business cards, and stationary created.

Pixel Forge created a logo for our business, and now we are wanting business cards, and stationary. I have included two designs of the same logo. Please feel free to use them as you want. The name of the company is Cedar Ridge Property Group LLC, the address is 812 NE Willow Ln., Suite 9, the city & state is Alder Falls, Montana, zip code is 97815, Telephone number is 555-327-4489, Fax number is 555-327-6051, the name on the business card is Carl Whitby CMCA

Industry/Entity Type

Property Management

Contact Information for Business Card

The card needs to look professional. Upscale.

Requirements
Must have
• The colors we are using are on the logo that has been uploaded.

```html
<!DOCTYPE html>
<html lang="en">
<head>
<meta charset="utf-8">
<title>Cedar Ridge Property Group – Business Card</title>
<link rel="stylesheet" href="https://fonts.googleapis.com/css2?family=Exo+2:wght@600;700&family=Gelasio:wght@400;700&display=swap">
<style>
  :root {
    --brand-green: #2bb962;
    --brand-navy: #243a5a;
    --paper: #ffffff;
  }
  * { margin: 0; padding: 0; box-sizing: border-box; }
  html, body {
    width: 1200px;
    height: 1000px;
    overflow: hidden;
    background: var(--paper);
  }
  .card {
    position: relative;
    width: 1200px;
    height: 1000px;
    background: var(--paper);
    color: var(--brand-navy);
    text-align: center;
  }
  .brand-mark {
    position: absolute;
    left: 556px;
    top: 228px;
    width: 88px;
    height: 88px;
    background: var(--brand-navy);
  }
  .brand-name {
    position: absolute;
    left: 0;
    right: 0;
    top: 350px;
    font-family: "Exo 2", sans-serif;
    font-weight: 700;
    font-size: 92px;
    line-height: 1;
    letter-spacing: 1px;
    color: var(--brand-green);
    text-transform: uppercase;
  }
  .descriptor {
    position: absolute;
    left: 292px;
    width: 590px;
    top: 452px;
    display: flex;
    align-items: center;
    gap: 18px;
    font-family: "Exo 2", sans-serif;
    font-weight: 700;
    font-size: 19px;
    letter-spacing: 2.5px;
    color: var(--brand-navy);
    text-transform: uppercase;
  }
  .descriptor::before,
  .descriptor::after {
    content: "";
    flex: 1;
    height: 3px;
    background: var(--brand-navy);
  }
  .tagline {
    position: absolute;
    left: 292px;
    width: 590px;
    top: 484px;
    display: flex;
    justify-content: space-between;
    font-family: "Exo 2", sans-serif;
    font-weight: 600;
    font-size: 17px;
    color: var(--brand-navy);
    text-transform: uppercase;
  }
  .contact-name {
    position: absolute;
    left: 0;
    right: 0;
    top: 546px;
    font-family: "Gelasio", serif;
    font-weight: 700;
    font-size: 39px;
    letter-spacing: 1px;
    color: var(--brand-green);
    text-transform: uppercase;
  }
  .contact-lines {
    position: absolute;
    left: 0;
    right: 0;
    top: 590px;
    font-family: "Gelasio", serif;
    font-size: 28px;
    line-height: 39px;
    color: var(--brand-navy);
    list-style: none;
  }
  .address {
    position: absolute;
    left: 0;
    right: 0;
    top: 694px;
    font-family: "Gelasio", serif;
    font-size: 29px;
    color: var(--brand-navy);
    text-transform: uppercase;
    word-spacing: 1px;
  }
  .address .sep { margin: 0 14px; }
</style>
</head>
<body>
  <main class="card">
    <div class="brand-mark" aria-hidden="true"></div>
    <h1 class="brand-name">Cedar Ridge</h1>
    <p class="descriptor">Property Management</p>
    <p class="tagline" aria-label="Rooted in service">
      <span>R</span><span>o</span><span>o</span><span>t</span><span>e</span><span>d</span>
      <span>&nbsp;</span>
      <span>i</span><span>n</span>
      <span>&nbsp;</span>
      <span>s</span><span>e</span><span>r</span><span>v</span><span>i</span><span>c</span><span>e</span>
    </p>
    <h2 class="contact-name">Carl Whitby, CMCA</h2>
    <ul class="contact-lines">
      <li class="phone">P: 555.327.4489</li>
      <li class="fax">F: 555.327.6051</li>
    </ul>
    <p class="address">812 NE Willow Ln.<span class="sep">•</span>Suite 9<span class="sep">•</span>Alder Falls, Montana 97815</p>
  </main>
</body>
</html>
```